New business card with our logo

we finalized our logo with the help of pixel harbor - now we need a business card using that logo. we are a metal service center providing raw steel and metal products for fabricating, contractors, artists, etc. we have the wording for the back of the card figured out (attached, no deviations from text please), just need help putting it all together.
would like the look of steel somehow incorporated in the design ... would like the black part of the logo to be steel or silver color (the S & BRANLEY)
Other font styles liked:
- calibri, arial, similar to those, modern looking
Colors
Designer to choose colors to be used in the design.
Requirements
Must have
- Back of card must haves are attached (no deviations from wording please).
- FRONT of card:
- logo
- address
- name
- office tel
- cell
- fax
- website
- address
Nice to have
- incorporate the look of steel or element of steel somehow
- names of the staff on front not in all caps, i.e. Rosvita not ROSVITA
- this industry is more industrial, not coffee or flower shop so design should be aligned with that
- design should be classic and tasteful

```html
<!DOCTYPE html>
<html lang="en">
<head>
<meta charset="utf-8">
<title>Branley Steel – Business Card</title>
<link href="https://fonts.googleapis.com/css2?family=Lato:wght@300;400;700;900&family=Oswald:wght@500;700&display=swap" rel="stylesheet">
<style>
  :root {
    --page: #2a2a2a;
    --card: #141414;
    --card-edge: #1d1d1d;
    --plate-a: #1c1c1c;
    --plate-b: #0c0c0c;
    --silver: #e6e6e6;
    --grey: #a8a8a8;
    --blue: #1d74c4;
    --rust: #c98a5e;
    --rust-light: #e2b89a;
    --steel-light: #f1ede8;
    --rule: #555555;
  }
  * { margin: 0; padding: 0; box-sizing: border-box; }
  html, body { width: 1200px; height: 997px; overflow: hidden; }
  body {
    background: var(--page);
    font-family: "Lato", Arial, sans-serif;
    color: var(--silver);
    position: relative;
  }
  .card {
    position: absolute;
    left: 220px;
    width: 760px;
    height: 434px;
    background: var(--card);
    border: 1px solid var(--card-edge);
    box-shadow: 0 12px 30px rgba(0,0,0,.55);
    overflow: hidden;
  }
  .card--front { top: 45px; }
  .card--back  { top: 518px; }
  .plate-texture {
    position: absolute; inset: 0;
    background: radial-gradient(ellipse at 55% 40%, var(--plate-a) 0%, var(--plate-b) 85%);
  }

  /* FRONT */
  .brand {
    position: absolute; left: 130px; top: 92px;
    display: flex; align-items: center; gap: 18px;
  }
  .brand__dot {
    width: 62px; height: 62px; border-radius: 50%;
    border: 6px solid var(--blue);
  }
  .brand__name {
    font-weight: 900; font-size: 46px; letter-spacing: 2px;
    color: var(--silver);
  }
  .person {
    position: absolute; left: 230px; top: 222px;
    text-align: right; width: 200px;
  }
  .person__name { font-size: 18px; font-weight: 300; color: var(--grey); }
  .person__name b { font-weight: 700; color: var(--silver); }
  .person__role { font-size: 14px; color: var(--grey); margin-top: 2px; }
  .person__address {
    margin-top: 26px; font-size: 18px; font-weight: 700; line-height: 1.35; color: var(--silver);
  }
  .divider {
    position: absolute; left: 455px; top: 212px;
    width: 1px; height: 120px; background: linear-gradient(var(--card), var(--grey), var(--card));
  }
  .contacts {
    position: absolute; left: 480px; top: 212px;
    list-style: none; font-size: 15px; color: var(--grey);
  }
  .contacts li { display: flex; align-items: center; gap: 10px; height: 27px; }
  .contacts svg { width: 14px; height: 14px; flex: none; }

  /* BACK */
  .headline {
    position: absolute; left: 0; right: 0; top: 44px; text-align: center;
    font-family: "Oswald", "Arial Narrow", sans-serif; text-transform: uppercase;
  }
  .headline__metal {
    font-weight: 700; font-size: 120px; line-height: 1; letter-spacing: 4px;
    color: var(--steel-light);
  }
  .headline__sub {
    font-weight: 700; font-size: 50px; line-height: 1; letter-spacing: 1px;
    color: var(--rust);
  }
  .rule {
    position: absolute; left: 130px; right: 130px; height: 1px; background: var(--rule);
  }
  .rule--top { top: 236px; }
  .services {
    position: absolute; left: 0; right: 0; top: 244px; text-align: center;
    font-size: 18px; letter-spacing: 1px; color: var(--silver);
  }
  .services .sep { color: var(--blue); margin: 0 8px; }
  .rule--bottom { top: 276px; }
  .products {
    position: absolute; left: 0; right: 0; top: 292px; text-align: center;
    font-size: 19px; line-height: 1.4; color: var(--grey);
  }
  .products em { font-style: normal; color: var(--rust-light); }
  .tagline {
    position: absolute; left: 0; right: 0; top: 376px; text-align: center;
    font-size: 21px; font-weight: 900; color: var(--rust);
  }
</style>
</head>
<body>

<section class="card card--front" aria-label="Card front">
  <div class="plate-texture" role="img" aria-label="Dark steel diamond tread plate texture"></div>

  <div class="brand">
    <span class="brand__dot"></span>
    <span class="brand__name">BRANLEY STEEL</span>
  </div>

  <div class="person">
    <p class="person__name">Darren <b>Okafor</b></p>
    <p class="person__role">Director</p>
    <p class="person__address">48 Foundry Row<br>Millbank</p>
  </div>

  <div class="divider"></div>

  <ul class="contacts">
    <li>
      <svg viewBox="0 0 14 14"><rect width="14" height="14" rx="2" fill="var(--blue)"/><path d="M4 3h2l1 2.5-1.2 1a6 6 0 0 0 2.7 2.7l1-1.2L12 9v2a1 1 0 0 1-1 1A8 8 0 0 1 3 4a1 1 0 0 1 1-1z" fill="#fff"/></svg>
      512.555.0142
    </li>
    <li>
      <svg viewBox="0 0 14 14"><rect width="14" height="14" rx="2" fill="var(--blue)"/><rect x="4.5" y="2.5" width="5" height="9" rx="1" fill="none" stroke="#fff"/></svg>
      512.555.0187
    </li>
    <li>
      <svg viewBox="0 0 14 14"><rect width="14" height="14" rx="2" fill="var(--blue)"/><rect x="2.5" y="4" width="9" height="6.5" fill="none" stroke="#fff"/><path d="M2.5 4l4.5 3.5L11.5 4" fill="none" stroke="#fff"/></svg>
      darren@branleysteel.com
    </li>
    <li>
      <svg viewBox="0 0 14 14"><rect width="14" height="14" rx="2" fill="var(--blue)"/><circle cx="7" cy="7" r="4.2" fill="none" stroke="#fff"/><path d="M2.8 7h8.4M7 2.8c-2 2.4-2 6 0 8.4M7 2.8c2 2.4 2 6 0 8.4" fill="none" stroke="#fff" stroke-width=".8"/></svg>
      www.branleysteel.com
    </li>
  </ul>
</section>

<section class="card card--back" aria-label="Card back">
  <div class="plate-texture" role="img" aria-label="Dark steel diamond tread plate texture"></div>

  <h1 class="headline">
    <span class="headline__metal">Metal</span><br>
    <span class="headline__sub">Service Center</span>
  </h1>

  <div class="rule rule--top"></div>
  <p class="services">CUT<span class="sep">●</span>SHEAR<span class="sep">●</span>PUNCH<span class="sep">●</span>LIGHT FAB</p>
  <div class="rule rule--bottom"></div>

  <p class="products">
    Str<em>uctural Steel</em>, Stainless &amp; Aluminum,<br>
    Building <em>Components</em>, Rebar, Decking.. &amp; more...
  </p>

  <p class="tagline">CUT TO SIZE, PICK-UP OR DELIVERED !</p>
</section>

</body>
</html>
```